Famous Australian Web Brand (SiteKeyHub.com.au) Needs a New Website & Logo

SiteKeyHub.com.au is one of the leading domain name registration businesses in Australia and is looking for an overhaul of its website and brand.

SiteKeyHub.com.au current products/services include domain name registration, web hosting, web site creation and SSL certificates.

In this design contest on PixelSwarm, we would like designers to create a new logo and new website design for SiteKeyHub.com.au.

Here is what contest entrants will need to create:
- 1 new logo
- 1 new home page design
- 1 internal page (pricing page)

The winning designer will receive the main prize of $750. In addition to this, the winning designer will have the opportunity to work with SiteKeyHub for the build of the full website and may get ongoing design work from SiteKeyHub.
Updates

thank you all for your designs, we are after a web 2.0 look and feel, please dont use serif fonts, lets use modern and sleek ones, i will upload some samples of one we like shortly

header is to be in black with some texturing, white fonts and the call to action buttons are in green.

for the 6 free services, please use round edges for the images with the text under it, as i will upload shortly and we would like custome images, not stockimage types please

im uploading a sample of a background image for the header, which is black with texturing and also and image for the footer/middle of the page which has the correct shading of the grey for the middle section

please see file 8 for the look we are trying to get with our site and for font ideas

Reason: we have decided to extend the contest for another 3 days as a couple of designers have requested a bit more time

Target Market(s)

People that might need to buy a domain name or start a website: small business owners; entrepreneurs; bloggers; everyone from mum-and-dad website owners to tech savvy entrepreneurs. Geographically we will be targeting Australia but this should not influence the design.

Industry/Entity Type

Build

Requirements
Must have
• The logo should:
- Have the text "SiteKeyHub"
- Be positioned in the top left hand corner of the website
- Be either a wordmark, pictorial or abstract logo. That is, text-only logos are acceptable but we are also interested in receiving logos with a mark to the left that could somehow represents the business that we’re in

The homepage should:
- Feel modern, slick, web2.0
- Have a horizontal menu with 4 menu items: About Us | Contact Us | My Cart | Login
- Include the logo at the top
- Include the content from this Word Document
- Include the rough layout and style from this JPG template layout

The interior page should:
- Have the same look and feel as the home page
- Include the rough layout and style from this JPG attachment
- Include the content from this second Word Document
Nice to have
• - Grey, white and black primary colors
- Buttons that are green or lime green with a web2.0 call to action
- Full-width design (i.e. across the screen like PixelSwarm)
Should not have
• - Do not include overt Australian references. While we are an Australian business we do not want Australian flags, kangaroos or Captain Bellwether in our logo or on our website.
- Do not use the current red color scheme in the design. We want to move away from this.

```html
<!DOCTYPE html>
<html lang="en">
<head>
<meta charset="utf-8">
<title>SiteKeyHub – Create a Free Website</title>
<link href="https://fonts.googleapis.com/css2?family=Arimo:wght@400;700&display=swap" rel="stylesheet">
<style>
:root{
  --black:#000;
  --ink:#333;
  --dark:#3b3b3b;
  --mid:#6b6b6b;
  --panel:#e4e4e4;
  --page:#fff;
  --green:#8dc63f;
  --green-dark:#6fa228;
  --green-light:#b9e06a;
  --rule:#c9c9c9;
  --white:#fff;
}
*{box-sizing:border-box;margin:0;padding:0}
html,body{width:1200px;height:2268px;overflow:hidden}
body{position:relative;background:var(--page);font-family:"Arimo",Arial,sans-serif;color:var(--ink)}
.abs{position:absolute}

/* header */
.site-header{left:0;top:0;width:1200px;height:330px;background:
  radial-gradient(ellipse 420px 260px at 880px 180px,#2a2a2a 0%,#111 60%,#000 100%);}
.top-nav{right:180px;top:0;height:42px;width:318px;background:#1a1a1a;border:1px solid #444;border-top:0;display:flex;align-items:center;justify-content:center;gap:14px;font-size:13px;font-weight:700;color:var(--white)}
.top-nav span.sep{color:#888;font-weight:400}
.phone{left:907px;top:54px;font-size:17px;font-weight:700;color:var(--white)}
.brand{left:214px;top:66px;display:flex;align-items:center;gap:14px;color:var(--white);font-size:46px;font-weight:400;letter-spacing:-1px}
.brand i{display:block;width:34px;height:34px;background:var(--green)}
.tagline{left:214px;top:200px;font-size:19px;font-weight:700;color:var(--white)}
.search{left:214px;top:232px;width:357px;height:30px;background:#3a3a3a;border:1px solid #555;font-size:11px;color:#ccc;display:flex;align-items:center;justify-content:space-between;padding:0 10px}
.search .field{flex:1;margin:0 8px;height:20px;background:#2a2a2a}
.quick-links{left:214px;top:273px;font-size:13px;color:#ccc;display:flex;gap:16px}
.quick-links span.dot{color:#aaa}

/* product column */
.column{left:183px;top:359px;width:839px;height:680px;background:var(--panel);border-radius:10px 10px 0 0}
.tabs{left:204px;top:338px;display:flex;gap:6px}
.tab{width:155px;height:42px;border-radius:8px 8px 0 0;background:linear-gradient(#d7f08e,var(--green) 55%,var(--green-dark));border:2px solid #fff;color:var(--white);font-size:16px;display:flex;align-items:center;justify-content:center}
.sheet{left:193px;top:380px;width:819px;height:650px;background:var(--white)}
.headline{left:312px;top:402px;font-size:27px;line-height:32px;color:var(--dark)}
.headline b{color:var(--green)}
.side-nav{left:191px;top:472px;width:102px}
.side-nav .feature{height:38px;background:var(--green);margin-bottom:10px}
.side-nav div.item{height:17px;background:var(--dark);color:var(--white);font-size:11px;line-height:17px;padding-left:8px;margin-bottom:9px}
.plan{top:480px;width:227px;height:507px;background:#f4f4f4;border-radius:8px 8px 0 0;overflow:hidden}
.plan-head{background:var(--dark);height:96px;color:var(--white);padding-top:8px;border-radius:8px 8px 0 0}
.plan-name{font-size:11px;font-weight:700;padding-left:16px}
.plan-price{margin-top:5px;height:30px;background:linear-gradient(var(--green-light),var(--green-dark));text-align:center;font-size:24px;font-weight:700;line-height:30px}
.plan-note{font-size:11px;line-height:13px;padding:5px 16px 0}
.plan-body{padding:6px 16px 0;font-size:11px;line-height:13px;color:var(--ink)}
.plan-body p{margin-bottom:4px}
.plan-body li{list-style:none;text-transform:uppercase;font-size:11px;line-height:19px;border-bottom:1px dotted var(--rule)}
.plan-body li:before{content:"";display:inline-block;width:5px;height:5px;background:var(--green);margin-right:8px;vertical-align:middle}
.plan-cta{position:absolute;left:0;bottom:0;width:100%;height:24px;background:linear-gradient(var(--green-light),var(--green-dark));color:var(--white);font-size:11px;font-weight:700;line-height:24px;padding-left:16px}

/* questions */
.faq-band{left:183px;top:1030px;width:839px;height:48px;background:#c9c9c9}
.faq-title{left:183px;top:1030px;width:310px;height:48px;background:#1c1c1c;color:var(--white);font-size:38px;line-height:48px;padding-left:56px;border-radius:0 0 10px 0}
.faq{left:183px;top:1078px;width:839px;height:1070px;background:var(--panel);border-radius:0 0 10px 10px}
.faq-col{top:1108px;width:397px}
.faq-col h3{font-size:17px;line-height:20px;color:var(--green);font-weight:700;position:relative;padding-left:20px;margin-bottom:4px}
.faq-col h3:before{content:"";position:absolute;left:0;top:6px;width:9px;height:9px;background:var(--mid)}
.faq-col p{font-size:13.4px;line-height:18px;color:#444;text-align:justify;padding-left:20px;margin-bottom:18px}

/* footer */
.site-footer{left:0;top:2150px;width:1200px;height:118px;background:var(--black)}
.foot-nav{left:191px;top:2165px;font-size:13px;font-weight:700;color:var(--white);display:flex;gap:12px}
.foot-nav span.sep{color:#888;font-weight:400}
.question-box{left:831px;top:2167px;width:189px;height:77px;border:1px solid #aaa;color:var(--white);text-align:center;font-size:12px;line-height:15px;padding-top:10px}
.question-box b{display:block;font-size:13px}
.copyright{left:183px;top:2233px;font-size:11px;color:#ccc}
</style>
</head>
<body>

<header class="abs site-header"></header>
<nav class="abs top-nav"><span>About Us</span><span class="sep">|</span><span>Contact Us</span><span class="sep">|</span><span>My Cart</span><span class="sep">|</span><span>Login</span></nav>
<div class="abs phone">1300 555 010</div>
<div class="abs brand"><i></i>SiteKeyHub</div>
<div class="abs tagline">You get a lot more than just a domain name</div>
<div class="abs search"><span>www.</span><span class="field"></span><span>.com</span></div>
<div class="abs quick-links"><span>Renew a domain</span><span class="dot">•</span><span>Transfer a domain</span><span class="dot">•</span><span>View Price List</span></div>

<div class="abs column"></div>
<div class="abs tabs">
  <div class="tab">Domains</div><div class="tab">Creator</div><div class="tab">Email</div><div class="tab">Hosting</div><div class="tab">Marketing</div>
</div>
<div class="abs sheet"></div>
<h1 class="abs headline" style="font-weight:400">Create a <b>FREE</b> Website Today.<br>Be Online for Your Customers Tomorrow.</h1>

<nav class="abs side-nav">
  <div class="feature"></div>
  <div class="item">Overview</div><div class="item">Features</div><div class="item">Pricing</div><div class="item">Hosting</div><div class="item">Social Media</div><div class="item">Searchly Tools</div><div class="item">Widgets</div><div class="item">SEO</div><div class="item">eCommerce</div><div class="item">Gallery</div><div class="item">Guides</div>
</nav>

<section class="abs plan" style="left:308px">
  <div class="plan-head"><div class="plan-name">FREE</div><div class="plan-price">$0</div><div class="plan-note">FREE for as long as your domain is registered with us</div></div>
  <div class="plan-body"><p>Gives you the tools you need to create a professional looking website with ease and it's completely free!</p>
  <ul><li>15 pages max</li><li>1 site per account</li><li>SiteForge</li><li>Hosting</li><li>1GB monthly bandwidth</li><li>20MB storage</li><li>Unlimited support</li><li>Over 4,000 designs</li><li>Membership tools</li><li>Video players</li><li>Picture galleries</li><li>MP3 jukeboxes</li><li>Widget library</li></ul></div>
  <div class="plan-cta">CREATE YOUR SITE</div>
</section>

<section class="abs plan" style="left:540px">
  <div class="plan-head"><div class="plan-name">LITE</div><div class="plan-price">$5.99/mo</div><div class="plan-note">Save 15% off all annual packages, only $59.99/pa</div></div>
  <div class="plan-body"><p>Comes with extra web space, so you can build a professional site in minutes and earn money from it with Searchly AdPlace</p>
  <ul><li>Unlimited pages</li><li>1 site per account</li><li>SiteForge</li><li>Hosting</li><li>6GB monthly bandwidth</li><li>50MB storage</li><li>Unlimited support</li><li>Over 4,000 designs</li><li>Membership tools</li><li>Video players</li><li>Picture galleries</li><li>MP3 jukeboxes</li><li>Widget library</li><li>Searchly AdPlace</li></ul></div>
  <div class="plan-cta">CREATE YOUR SITE</div>
</section>

<section class="abs plan" style="left:780px">
  <div class="plan-head"><div class="plan-name">STANDARD</div><div class="plan-price">$11.99/mo</div><div class="plan-note">Save 15% off all annual packages, only $119.99/pa</div></div>
  <div class="plan-body"><p>Gives you access to ecommerce features, allows you to build up to 5 sites and provides more disk space and bandwidth.</p>
  <ul><li>Unlimited pages</li><li>5 site per account</li><li>SiteForge</li><li>Hosting</li><li>10GB bandwidth</li><li>250MB storage</li><li>Unlimited support</li><li>Over 4,000 designs</li><li>Membership tools</li><li>Video players</li><li>Picture galleries</li><li>MP3 jukeboxes</li><li>Widget library</li><li>Searchly AdPlace</li><li>Commerce tools</li></ul></div>
  <div class="plan-cta">CREATE YOUR SITE</div>
</section>

<div class="abs faq-band"></div>
<h2 class="abs faq-title" style="font-weight:400">Questions</h2>
<div class="abs faq"></div>

<div class="abs faq-col" style="left:198px">
  <h3>What is SiteForge?</h3>
  <p>SiteForge is a multiple award-winning website building service that allows you to quickly and easily create professional looking websites. SiteForge is simple to use and packed with powerful features allowing you to achieve results beyond your expectations! SiteForge has been around since Jan 2000, with over 3,000,000 sites built using this technology. SiteForge was released in Nov 2004 and is the latest in this award-winning series. It was awarded the Best Application Award at the Motion Web Awards 2005 in San Francisco.</p>
  <h3>What should I use SiteForge for?</h3>
  <p>SiteForge can be used for any kind of website or online content. From personal profile pages to e-commerce stores, SiteForge makes publishing and designing your website quick and easy. We are constantly surprised by the kinds of sites that our customers build which vary hugely in their purpose, style, structure and language. To get inspired by some of the sites that have been built using SiteForge have a look at our Gallery Page.</p>
  <h3>Why is SiteForge different from other website builders?</h3>
  <p>SiteForge is different from other website builders because of its unparalleled ease of use. We offer a true 'drag and drop, point and click' edit environment which makes it incredibly easy to update your content. If you want to change some text, just click on it on your site and change it. If you want to move an image, just drag it across the page, or drag the corners to change its size. There is no technology to learn, no code, no form filling, just quick and easy tools that work intuitively. There is a free no-obligation trial, so why not have a go.</p>
  <h3>Does SiteForge work well with search engines?</h3>
  <p>Yes it does. SiteForge makes all of your content visible to search engines in standards compliant HTML which allows them to easily index and rank your pages. Additionally, SiteForge gives you the option to add page titles, keywords and descriptions for every page in your site, and we automatically produce a Sitemap document for your site which gives search engines a complete list of your visible pages. If you don't want your pages listed by search engines, we allow you to make them invisible too. Many of our sites rank extremely highly on search engines.</p>
  <h3>How do I publish my SiteForge site?</h3>
  <p>SiteForge sites are always 'live' online, i.e. you don't have to publish them. Your pages are always available to people visiting your site and changes that you make happen instantaneously. We also enable you to hide pages from the menu while you are editing them if you prefer.</p>
</div>

<div class="abs faq-col" style="left:608px">
  <h3>Can I sell things on SiteForge?</h3>
  <p>Yes you can. SiteForge currently integrates with CoinPost as a payment gateway. You can set up links or buttons on your site to act as 'buy now' or 'add to cart' CoinPost buttons. CoinPost is a free service which allows you to send and receive payments online and it allows your customers to manage a shopping cart of items. SiteForge allows you to integrate with these features for your own online store.</p>
  <h3>Can I use SiteForge to build sites for other people?</h3>
  <p>Definitely, this is something that is quite common. Many web designers find SiteForge to be a very useful tool that allows them to quickly build and design sites for clients as there are no technology headaches to deal with. And you can offer the client a free content management tool built in! However, if you are selling sites built using SiteForge we require that you purchase a new account for each client. It is against our Terms to use a single Standard account to host multiple paid client sites.</p>
  <h3>Can I use Searchly tools (Site Console, Sitemaps, AdPlace, Insights, AdBid)?</h3>
  <p>All of them. SiteForge allows you to place Searchly AdPlace adverts on your site enabling you to make money from the clicks-throughs. You can also buy AdBid on Searchly to drive traffic to your site. Tracking user activity and page views on your site can be achieved by using Searchly Insights which you can easily sign up for through your site. Furthermore, we allow you to use Searchly Site Console and automatically produce a Sitemap for your site that helps search engines index your pages.</p>
  <h3>Can I get help if I can't use it?</h3>
  <p>Yes. We have a number of different support channels available. Firstly our Product FAQs offer answers to the most common questions and should be able to help you with most of your issues, along with a beginner's guide which is available to download. For anything else you can submit an email query to our support team who will answer it within 24 hours. There is also a product forum in our Community section that allows site builders to share tips and experiences building sites using SiteForge.</p>
  <h3>SiteForge is built using Vectra Motion, why? Does it matter?</h3>
  <p>The SiteForge editing tools are built using Vectra Motion because it allows us to offer a genuine 'drag and drop' WYSIWYG interface that makes SiteForge so easy to use. However, we publish your site in both Vectra and HTML so it is available to the widest range of browsers and is correctly indexed and listed by search engines. Vectra is often criticised for not being search engine friendly, which is why we extract the content from your site and publish it in HTML too. So you get all the benefits of a slick easy to use Vectra interface without any downside. That is why SiteForge is an awesome tool.</p>
</div>

<footer class="abs site-footer"></footer>
<nav class="abs foot-nav"><span>About Us</span><span class="sep">|</span><span>Contact Us</span><span class="sep">|</span><span>My Cart</span><span class="sep">|</span><span>Login</span></nav>
<div class="abs question-box">HAVE A QUESTION FOR US?<b>CONTACT US</b><b>1300 555 010</b></div>
<div class="abs copyright">2010 sitekeyhub.com.au. Tout droits réservés. Site créé par Atelierweb 2010 créateur de boutique en ligne Shopnova</div>

</body>
</html>
```